Buch-/eBook-Cover für Lern- und Prüfungscoaching
Zielgruppe
Lernende, Erwachsene, Eltern
Mein Unternehmen bietet Lerncoaching und Prüfungscoaching für Studenten und Schüler an.
Das Buch ist für lernende, die sich mit Ihren eigenen Lernweg beschäftigen wollen.
Aufgabenstellung
Ich benötige ein ansprechendes Buch-Cover. Das Format für das Buch ist 15,24 x 22,86 cm (6' x 9').
Mein Buch Cover soll sich aber deutlich von den anderen Büchern abheben und Erwachsene ansprechen.
Wichtig ist mir auch einen Wiedererkennungswert vom Buch-Cover zu haben.
Bitte um ein ansprechendes Bild, denn ich möchte mich deutlich von meiner Konkurrenz abheben.
Buchtitel: Entwirf deine Wissensreise
Untertitel: Entdecke deine eigene Spur zum Ziel!
Autorin: Helga Brosowski
Das Buch soll meinen bisherigen Büchern in der Stilrichtung entsprechen. Der Hintergrund in demselben Blau. https://www.buchkiosk-beispiel.de/dp/X7QK52PLVT
Elemente vom Cover:
aufgeschlagenes Buch (dynamisch) Weg vom Buch weg eine Person unisex (symbolisch) auf den Weg, bunte Stifte
Lernweg im Leben eines Menschen
Text für den Buchrücken:
Entwirf deine Wissensreise: Entdecke deinen individuellen Weg zum erfolgreichen Lernen
Du hast es in der Hand! Deine Lernbiografie ist einzigartig – genau wie du. In diesem Buch lernst du, wie du deine persönliche Lerngeschichte erkennst und sie gezielt nutzt, um deine Lernziele mit Leichtigkeit und Motivation zu erreichen. Ob Prüfungsstress, fehlende Motivation oder unklare Lernstrategien – hier findest du praktische Tipps, die genau zu dir passen.
Lerne, wie du:
• Effektive Lernstrategien entwickelst, die für dich funktionieren
• Deine Stärken und Erfahrungen einsetzt, um dein volles Potenzial zu entfalten
• Blackouts und Stress in Prüfungen überwindest
• Deine Zeit besser managst und dabei noch Zeit für Spaß hast
• Deine Lernziele klar und motivierend definierst
Dieses Buch zeigt dir Schritt für Schritt, wie du aus deinen bisherigen Lernerfahrungen lernst und sie in deine Erfolgsstrategie verwandelst. Egal, ob du gerade für die nächste Prüfung lernst oder deinen Lernweg langfristig optimieren mÃ..

```html
<!DOCTYPE html>
<html lang="de">
<head>
<meta charset="utf-8">
<title>Entwirf deine Wissensreise – Buchumschlag</title>
<link href="https://fonts.googleapis.com/css2?family=Playfair+Display:wght@400;500&family=Amatic+SC:wght@700&family=Mouse+Memoirs&display=swap" rel="stylesheet">
<style>
  :root {
    --stage: #000000;
    --cover-blue: #4596c8;
    --sky-light: #bcd6e2;
    --accent-yellow: #e4e332;
    --ink-navy: #2b2a78;
    --title-red: #e84c4a;
    --paper-white: #ffffff;
    --meadow: #d8e225;
    --meadow-light: #e2e64a;
    --path-cream: #f3e8cf;
    --page-grey: #e4e4e4;
  }
  * { margin: 0; padding: 0; box-sizing: border-box; }
  html, body { width: 1200px; height: 895px; overflow: hidden; background: var(--stage); }
  .canvas { position: relative; width: 1200px; height: 895px; }
  .cover { position: absolute; left: 67px; top: 59px; width: 1066px; height: 778px; overflow: hidden; }
  .serif { font-family: "Playfair Display", Georgia, serif; }
  .hand { font-family: "Amatic SC", "Arial Narrow", sans-serif; font-weight: 700; }

  /* back cover */
  .back { position: absolute; left: 0; top: 0; width: 548px; height: 778px; background: var(--cover-blue); text-align: center; }
  .back-headline { position: absolute; left: 0; right: 0; top: 44px; font-size: 29px; color: var(--accent-yellow); letter-spacing: 0.5px; }
  .back-subline { position: absolute; left: 0; right: 0; top: 84px; font-size: 19px; line-height: 22px; color: var(--accent-yellow); }
  .dots { border-top: 3px dotted; height: 0; position: absolute; }
  .back-dots { left: 191px; width: 136px; top: 142px; border-color: var(--ink-navy); }
  .blurb { position: absolute; left: 44px; width: 428px; font-size: 13.6px; line-height: 16.8px; color: var(--paper-white); font-weight: 400; }
  .blurb-intro { top: 189px; }
  .blurb-outro { top: 512px; }
  .learn-heading { position: absolute; left: 48px; top: 306px; padding: 0 8px 0 7px; font-size: 30px; color: var(--ink-navy); border-bottom: 2px solid var(--ink-navy); line-height: 32px; text-align: left; }
  .learn-list { position: absolute; left: 43px; top: 355px; list-style: none; text-align: left; color: var(--ink-navy); font-size: 22px; line-height: 19px; }
  .learn-list li { margin-bottom: 5px; padding-left: 10px; text-indent: -10px; white-space: nowrap; }
  .learn-list li::before { content: "• "; }
  .tagline { position: absolute; left: 0; right: 0; top: 676px; font-size: 31px; line-height: 29px; color: var(--ink-navy); }

  /* spine */
  .spine { position: absolute; left: 523px; top: 0; width: 25px; height: 778px; }
  .spine-title, .spine-author { position: absolute; left: 2px; writing-mode: vertical-rl; transform: rotate(180deg); white-space: nowrap; }
  .spine-title { top: 52px; color: var(--accent-yellow); font-size: 11.5px; }
  .spine-title .hand { font-size: 15px; }
  .spine-author { top: 653px; color: var(--ink-navy); font-size: 11px; letter-spacing: 1px; }
  .spine-edge { position: absolute; left: 548px; top: 0; width: 1px; height: 778px; background: rgba(0,0,0,0.15); }

  /* front cover */
  .front { position: absolute; left: 548px; top: 0; width: 518px; height: 778px; background: linear-gradient(to bottom, var(--cover-blue) 0%, #7db0d2 40%, var(--sky-light) 78%); text-align: center; }
  .author { position: absolute; left: 0; right: 0; top: 42px; font-size: 32px; color: var(--accent-yellow); letter-spacing: 0.5px; }
  .front-dots { left: 96px; width: 326px; top: 123px; border-color: var(--accent-yellow); }
  .title-top { position: absolute; left: 0; right: 0; top: 153px; font-size: 50px; line-height: 60px; color: var(--paper-white); letter-spacing: 1px; font-weight: 400; }
  .title-main { position: absolute; left: 0; right: 0; top: 210px; font-family: "Mouse Memoirs", "Arial Narrow", sans-serif; font-size: 88px; line-height: 88px; color: var(--title-red); letter-spacing: -1px; font-weight: 400; }
  .subtitle { position: absolute; left: 0; right: 0; top: 305px; font-size: 17.5px; color: var(--ink-navy); }
  .illustration { position: absolute; left: 0; top: 348px; width: 518px; height: 430px; }
</style>
</head>
<body>
<div class="canvas">
  <div class="cover">
    <section class="back">
      <h2 class="back-headline hand">Entwirf deine Wissensreise:</h2>
      <p class="back-subline serif">Entdecke deinen individuellen<br>Weg zum erfolgreichen Lernen!</p>
      <div class="dots back-dots"></div>
      <p class="blurb blurb-intro serif">Du hast es in der Hand! Deine Lernbiografie ist einzigartig – genau wie du. In diesem Buch lernst du, wie du deine persönliche Lerngeschichte erkennst und sie gezielt nutzt, um deine Lernziele mit Leichtigkeit und Motivation zu erreichen. Ob Prüfungsstress, fehlende Motivation oder unklare Lernstrategien – hier findest du praktische Tipps, die genau zu dir passen.</p>
      <h3 class="learn-heading hand">Du lernst:</h3>
      <ul class="learn-list hand">
        <li>Effektive Lernstrategien entwickelst, die für dich funktionieren</li>
        <li>Deine Stärken und Erfahrungen einsetzt,<br>um dein volles Potenzial zu entfalten</li>
        <li>Blackouts und Stress in Prüfungen überwindest</li>
        <li>Deine Zeit besser managst und dabei noch Zeit für Spaß hast</li>
        <li>Deine Lernziele klar und motivierend definierst</li>
      </ul>
      <p class="blurb blurb-outro serif">Dieses Buch zeigt dir Schritt für Schritt, wie du aus deinen bisherigen Lernerfahrungen lernst und sie in deine Erfolgsstrategie verwandelst. Egal, ob du gerade für die nächste Prüfung lernst oder deinen Lernweg langfristig optimieren möchtest – du kannst es schaffen! Lass dich von deiner eigenen Lernbiografie inspirieren und entdecke den Weg zu mehr Spaß, Erfolg und Selbstvertrauen beim Lernen.</p>
      <p class="tagline hand">Entwirf deine Wissensreise -<br>Dein Schlüssel zum Lernerfolg!</p>
    </section>

    <div class="spine">
      <p class="spine-title serif"><span class="hand">Entwirf deine Wissensreise:</span> Entdecke deinen individuellen Lernweg zum Erfolg!</p>
      <p class="spine-author serif">HELGA BROSOWSKI</p>
    </div>
    <div class="spine-edge"></div>

    <section class="front">
      <p class="author serif">Helga Brosowski</p>
      <div class="dots front-dots"></div>
      <h1>
        <span class="title-top serif">ENTWIRF DEINE</span>
        <span class="title-main">WISSENSREISE</span>
      </h1>
      <p class="subtitle serif">Entdecke deine eigene Spur zum Ziel!</p>
      <svg class="illustration" viewBox="0 0 518 430">
        <defs>
          <linearGradient id="meadowFill" x1="0" y1="0" x2="0" y2="1">
            <stop offset="0" stop-color="var(--meadow)"/>
            <stop offset="1" stop-color="var(--meadow-light)"/>
          </linearGradient>
          <linearGradient id="sceneFill" x1="0" y1="0" x2="0" y2="1">
            <stop offset="0" stop-color="var(--path-cream)"/>
            <stop offset="0.6" stop-color="var(--paper-white)"/>
            <stop offset="1" stop-color="var(--page-grey)"/>
          </linearGradient>
        </defs>
        <path d="M0 200 C40 80 110 12 180 8 C240 5 290 40 340 30 C400 18 470 25 518 48 L518 430 L0 430 Z" fill="url(#meadowFill)"/>
        <rect class="scene-placeholder" x="36" y="100" width="446" height="308" rx="18" fill="url(#sceneFill)" role="img" aria-label="Illustration: aufgeschlagenes Buch, aus dem ein Weg in die Ferne führt, eine Person mit Gießkanne auf den Seiten, bunte Stifte, Pflanzen und eine Glühbirne"/>
      </svg>
    </section>
  </div>
</div>
</body>
</html>
```